Business Card Design Project

We need a business card design for a relatively new company called Velmar Gear. We design paddle (an outdoor winter sport primarily played in the midwest and east coast) and tennis bags for women and men. Velmar Gear is a lifestyle brand for the next generation country club goers. Our bags merge fashion with functionality and are making country club sports trendier and more fashionable.

I would like to include space for
Name: (will fill this in for employees)
Velmar Gear
Phone: (will do this)
Email:
www.velmargear.example

Would also like to include Chatterbook and Flitter icons.
Please do not use pictures of the bags - this is just to give you an idea of what style bags we sell.

Target Market(s)

30 to 40 year old men and women - luxury market

Industry/Entity Type

Fashion

Requirements
Must have
• Would like the company logo included

```html
<!DOCTYPE html>
<html lang="en">
<head>
<meta charset="utf-8">
<title>Velmar Gear — Business Card</title>
<link rel="stylesheet" href="https://fonts.googleapis.com/css2?family=Didact+Gothic&display=swap">
<style>
  :root {
    --card-bg: #000000;
    --text-light: #f2f2f2;
    --text-soft: #e6e6e6;
    --mark-grey: #9a9a9a;
  }
  html, body {
    margin: 0;
    padding: 0;
    width: 1200px;
    height: 739px;
    overflow: hidden;
    background: var(--card-bg);
  }
  .card {
    position: relative;
    width: 1200px;
    height: 739px;
    background: var(--card-bg);
    font-family: "Didact Gothic", "Century Gothic", sans-serif;
    color: var(--text-light);
  }
  .contact {
    position: absolute;
    right: 64px;
    top: 98px;
    text-align: right;
  }
  .contact__name {
    margin: 0 0 26px;
    font-size: 31px;
    letter-spacing: 0.5px;
    line-height: 1;
    color: var(--text-light);
  }
  .contact__list {
    list-style: none;
    margin: 0;
    padding: 0;
    font-size: 27px;
    line-height: 30px;
    color: var(--text-soft);
  }
  .brand {
    position: absolute;
    left: 86px;
    top: 474px;
    width: 340px;
    text-align: center;
  }
  .brand__dot {
    display: block;
    margin: 0 auto 22px;
  }
  .brand__name {
    margin: 0;
    font-size: 46px;
    line-height: 1;
    letter-spacing: 1px;
    font-weight: 400;
    color: var(--text-light);
    white-space: nowrap;
  }
</style>
</head>
<body>
  <div class="card">
    <section class="contact">
      <p class="contact__name">Name Of Employee</p>
      <ul class="contact__list">
        <li>Velmar Gear</li>
        <li>+91 9012345678</li>
        <li>name@velmargear.example</li>
        <li>www.velmargear.example</li>
      </ul>
    </section>

    <section class="brand">
      <svg class="brand__dot" width="100" height="100" viewBox="0 0 100 100" aria-hidden="true">
        <circle cx="50" cy="50" r="48" fill="var(--mark-grey)"/>
      </svg>
      <p class="brand__name">VELMAR GEAR</p>
    </section>
  </div>
</body>
</html>
```